Flyer-Design für Tierphysiotherapie und Osteopathie
Zielgruppe
Tierphysiotherapie und Osteopathie Lotte Brenner
Aufgabenstellung
Text des gewünschten Flyers ist hochgeladen.
Ebenso die Visitenkarten und das Logo, sowie die Website - zur Orientierung von Farben, Schriftarten, etc.
Auch ein paar Bilder sind beigefügt.

```html
<!DOCTYPE html>
<html lang="de">
<head>
<meta charset="utf-8">
<title>Flyer Tierphysiotherapie Lotte Brenner</title>
<link rel="stylesheet" href="https://fonts.googleapis.com/css2?family=Bebas+Neue&family=PT+Sans:wght@400;700&family=Montserrat:wght@400;500&display=swap">
<style>
  :root {
    --backdrop: #c3c6ce;
    --paper: #ffffff;
    --taupe: #7a6e68;
    --peach: #f9d99d;
    --stone: #d7d1ce;
    --amber: #f0b22f;
    --amber-text: #f0b22f;
    --ink: #6e625c;
    --white: #ffffff;
  }
  * { box-sizing: border-box; margin: 0; padding: 0; }
  html, body { width: 1200px; height: 782px; overflow: hidden; }
  body {
    background: var(--backdrop);
    font-family: "PT Sans", sans-serif;
    position: relative;
  }
  .page {
    position: absolute;
    top: 121px;
    width: 540px;
    height: 540px;
    background: var(--paper);
    padding: 14px;
    box-shadow: 0 6px 18px rgba(60, 60, 70, 0.25);
    overflow: hidden;
  }
  .page--inside { left: 40px; }
  .page--cover { left: 620px; }
  .grid {
    display: grid;
    grid-template-columns: repeat(2, minmax(0, 1fr));
    grid-template-rows: repeat(2, minmax(0, 1fr));
    width: 100%;
    height: 100%;
  }
  .cell {
    padding: 16px;
    font-size: 11.5px;
    line-height: 1.24;
    overflow: hidden;
    min-width: 0;
    min-height: 0;
    hyphens: auto;
  }
  .cell--taupe { background: var(--taupe); color: var(--amber-text); }
  .cell--peach { background: var(--peach); color: var(--ink); }
  .cell--stone { background: var(--stone); color: var(--ink); }
  .cell--amber { background: var(--amber); color: var(--white); }

  .intro-title { font-weight: 700; font-size: 12px; margin-bottom: 8px; }
  .intro-text { text-align: justify; margin-bottom: 8px; }

  .wish-title { font-weight: 700; font-size: 12px; margin-bottom: 4px; }
  .bullets { list-style: none; }
  .bullets li { position: relative; padding-left: 14px; margin-bottom: 6px; }
  .bullets li::before { content: "•"; position: absolute; left: 2px; font-size: 9px; top: 1px; }
  .bullets--tight li { margin-bottom: 1px; }

  .services { margin: 2px 0 10px 16px; }
  .emphasis { font-weight: 700; margin-bottom: 6px; }
  .closing-call { font-weight: 700; margin: 10px 0 12px; }

  .contact { font-family: "Montserrat", sans-serif; font-size: 9.5px; letter-spacing: 1px; }
  .contact-row { display: flex; align-items: center; gap: 8px; margin-bottom: 6px; white-space: nowrap; }
  .contact-row svg { width: 12px; height: 12px; flex: none; }

  .photo { width: 100%; height: 100%; }
  .photo--horse { background: linear-gradient(135deg, #6b3b22 0%, #8a5a3a 45%, #4fa9b0 80%, #3d2a22 100%); }
  .photo--dog { background: linear-gradient(160deg, #a8b49a 0%, #6f8e4a 40%, #b492c8 65%, #4d3024 100%); }

  .brand-cell { display: flex; align-items: center; justify-content: center; gap: 10px; }
  .brand-dot { width: 12px; height: 12px; border-radius: 50%; background: var(--amber); flex: none; }
  .brand-name { font-family: "PT Sans", sans-serif; font-size: 22px; font-weight: 400; color: var(--white); white-space: nowrap; }

  .cover-contact { display: flex; flex-direction: column; justify-content: center; padding: 20px 16px; }
  .cover-name { font-family: "Bebas Neue", sans-serif; font-size: 32px; font-weight: 400; letter-spacing: 2px; line-height: 1; white-space: nowrap; }
  .cover-role { font-family: "Montserrat", sans-serif; font-size: 9.5px; letter-spacing: 0.8px; margin: 6px 0 16px; white-space: nowrap; }
</style>
</head>
<body>

<section class="page page--inside" aria-label="Flyer Innenseite">
  <div class="grid">
    <div class="cell cell--taupe">
      <p class="intro-title">Ich heiße Lotte Brenner und bin Physio&shy;therapeutin und Osteopathin für Tiere</p>
      <p class="intro-text">Einschränkungen, Blockaden oder Schmerzen können viele Ursachen haben und äußern sich bei jedem Tier anders. Ihr Tier ist einzigartig, deshalb bekommen Sie bei mir die Behandlung, die zu Ihrem Tier und Ihnen passt!</p>
      <p class="intro-text">Neben der Arbeit mit meinen Händen biete ich unterschiedliche Therapieformen und Leistungen an wie z.B.:</p>
    </div>
    <div class="cell cell--peach">
      <p class="wish-title">Sie möchten:</p>
      <ul class="bullets">
        <li>Ihrem Jungtier einen guten Start ins Leben ermöglichen?</li>
        <li>Ihr Tier langfristig fit erhalten, um bis ins hohe Alter viele schöne Jahre voller gemeinsamer Erlebnisse zu haben?</li>
        <li>Ihren Sportpartner optimal begleiten?</li>
        <li>Durch regelmäßige Kontrollen Probleme frühzeitig erkennen oder einfach doch mal vorbeugen?</li>
      </ul>
    </div>
    <div class="cell cell--stone">
      <ul class="bullets bullets--tight services">
        <li>Lasertherapie</li>
        <li>Neurostim</li>
        <li>aktives und passives Bewegungstraining</li>
        <li>gezielter Muskelaufbau</li>
        <li>und vieles mehr</li>
      </ul>
      <p class="emphasis">Ich gehe ganz besonders auf die speziellen Bedürfnisse Ihres Tiere ein.</p>
      <p>Und begleite Sie und Ihr Tier liebevoll und einfühlsam. Gemeinsam finden wir den besten Weg zu mehr Bewegung und Lebensfreude!</p>
    </div>
    <div class="cell cell--amber">
      <ul class="bullets">
        <li>bei Beschwerden im Bewegungsapparat wie z.B. Arthrose, Bandscheibenvorfällen, neurologischen Einschränkungen oder Verletzungen mit Ihrem Tier kompetent und mit Gefühl unterstützt werden?</li>
      </ul>
      <p class="closing-call">Dann sind Sie bei mir genau richtig!</p>
      <div class="contact">
        <div class="contact-row">
          <svg viewBox="0 0 16 16" aria-hidden="true"><path fill="#fff" d="M3.5 1.5l2.5 0 1.2 3-1.6 1.2c.8 1.8 2 3 3.8 3.8l1.2-1.6 3 1.2v2.5c0 .8-.7 1.4-1.5 1.4C6.6 13 3 9.4 2.1 3c0-.8.6-1.5 1.4-1.5z"/></svg>
          <span>0160/5571238</span>
        </div>
        <div class="contact-row">
          <svg viewBox="0 0 16 16" aria-hidden="true"><rect x="1" y="3.5" width="14" height="9" fill="#fff"/><path d="M1.5 4l6.5 5 6.5-5" fill="none" stroke="#f0b22f" stroke-width="1.3"/></svg>
          <span>info@tierphysio-brenner.de</span>
        </div>
      </div>
    </div>
  </div>
</section>

<section class="page page--cover" aria-label="Flyer Titelseite">
  <div class="grid">
    <div class="cell cell--taupe brand-cell">
      <span class="brand-dot"></span>
      <span class="brand-name">Lotte Brenner</span>
    </div>
    <div class="photo photo--horse" role="img" aria-label="Foto: Therapeutin im türkisen Shirt mit braunem Pferd vor einem Holzstall"></div>
    <div class="photo photo--dog" role="img" aria-label="Foto: Therapeutin sitzt auf der Wiese und behandelt einen braunen Hund"></div>
    <div class="cell cell--amber cover-contact">
      <h1 class="cover-name">Lotte Brenner</h1>
      <p class="cover-role">Tierphysiotherapie &amp; Osteopathie</p>
      <div class="contact">
        <div class="contact-row">
          <svg viewBox="0 0 16 16" aria-hidden="true"><path fill="#fff" d="M3.5 1.5l2.5 0 1.2 3-1.6 1.2c.8 1.8 2 3 3.8 3.8l1.2-1.6 3 1.2v2.5c0 .8-.7 1.4-1.5 1.4C6.6 13 3 9.4 2.1 3c0-.8.6-1.5 1.4-1.5z"/></svg>
          <span>0160/5571238</span>
        </div>
        <div class="contact-row">
          <svg viewBox="0 0 16 16" aria-hidden="true"><rect x="1" y="3.5" width="14" height="9" fill="#fff"/><path d="M1.5 4l6.5 5 6.5-5" fill="none" stroke="#f0b22f" stroke-width="1.3"/></svg>
          <span>info@tierphysio-brenner.de</span>
        </div>
      </div>
    </div>
  </div>
</section>

</body>
</html>
```